Joan Pelley Letter Head

log and letter head

would like a modern feminine approch, please see attached the back of my business card

Joan Pelley Consulting

ABN 81 305 642 918

Address19a Brood Street Larkfield North 6042 Eastvale Territory

Business

```html
<!DOCTYPE html>
<html lang="en">
<head>
<meta charset="utf-8">
<title>Joan Pelley Consulting Letterhead</title>
<link rel="stylesheet" href="https://fonts.googleapis.com/css2?family=Raleway:wght@400;500&display=swap">
<style>
  :root {
    --paper: #ffffff;
    --brand-red: #c8202b;
    --blush: #f6dcdc;
    --blush-soft: #fbeeee;
    --ink-grey: #9a9a9a;
    --on-red: #ffffff;
  }
  * { margin: 0; padding: 0; box-sizing: border-box; }
  html, body {
    width: 851px;
    height: 1200px;
    overflow: hidden;
    background: var(--paper);
  }
  .letterhead {
    position: relative;
    width: 851px;
    height: 1200px;
    background: var(--paper);
    font-family: "Raleway", Arial, sans-serif;
  }
  .header-wash {
    position: absolute;
    top: 0;
    left: 0;
    width: 851px;
    height: 118px;
    background: linear-gradient(90deg, var(--blush-soft) 0%, var(--blush) 30%, var(--blush-soft) 50%, var(--blush) 72%, var(--blush-soft) 100%);
    opacity: 0.7;
  }
  .brand-name {
    position: absolute;
    top: 52px;
    left: 0;
    width: 851px;
    text-align: center;
    font-size: 40px;
    font-weight: 500;
    letter-spacing: 1px;
    color: var(--brand-red);
    line-height: 1;
  }
  .consulting-band {
    position: absolute;
    top: 118px;
    left: 0;
    width: 851px;
    height: 16px;
    background: var(--brand-red);
    display: flex;
    align-items: center;
    justify-content: center;
  }
  .consulting-band span {
    font-size: 10px;
    font-weight: 500;
    letter-spacing: 14px;
    color: var(--on-red);
    padding-left: 14px;
  }
  .contact-line {
    position: absolute;
    top: 143px;
    left: 0;
    width: 851px;
    text-align: center;
    font-size: 13px;
    font-weight: 400;
    color: var(--ink-grey);
    letter-spacing: 0.3px;
    white-space: nowrap;
  }
  .corner-block {
    position: absolute;
    left: 794px;
    top: 1080px;
    width: 57px;
    height: 84px;
    background: var(--brand-red);
  }
</style>
</head>
<body>
  <div class="letterhead">
    <div class="header-wash" role="img" aria-label="Faint oversized script name decoration across the top in soft pink"></div>
    <div class="brand-name">Joan Pelley</div>
    <div class="consulting-band"><span>CONSULTING</span></div>
    <p class="contact-line">ABN 81 305 642 918 Address 47c Tallow Street Larkfield North, 6042, Eastvale Territory</p>
    <div class="corner-block"></div>
  </div>
</body>
</html>
```